Stationery (Business Cards, Letterheads & Envelopes)

Require stationery design which includes the following items as a minimum.

- Business card design
- Letterhead
- Envelopes

Details for business card:
Logo: Main logo is called "tovell interiors square gold" but you may make use of whichever logo works best.
Tagline: Exquisite Furniture & Furnishings
Name: Mirren Oskaby
Title: Interior Stylist
Mobile: 0427 318 942
PH: 03 9512 3470
Email: mirren@tovell-interiors.com.au

Industry/Entity Type

Business

```html
<!DOCTYPE html>
<html lang="en">
<head>
<meta charset="utf-8">
<title>Tovell Interiors – Envelopes</title>
<link rel="stylesheet" href="https://fonts.googleapis.com/css2?family=Tinos&display=swap">
<style>
  :root {
    --backdrop: #d9d9d9;
    --paper: #f7f7f7;
    --paper-edge: #e4e4e4;
    --flap: #2f2f2f;
    --ink: #555555;
    --ink-soft: #6a6a6a;
  }
  * { margin: 0; padding: 0; box-sizing: border-box; }
  html, body { width: 1200px; height: 800px; overflow: hidden; }
  body {
    background: var(--backdrop);
    position: relative;
    font-family: "Tinos", "Times New Roman", serif;
  }
  .envelope {
    position: absolute;
    width: 500px;
    height: 250px;
    background: var(--paper);
    border: 1px solid var(--paper-edge);
    box-shadow: 0 6px 14px rgba(0,0,0,0.12);
  }
  .envelope--back { left: 120px; top: 150px; }
  .envelope--front { left: 580px; top: 400px; }

  .envelope__flap {
    position: absolute;
    left: 0; top: 0;
    width: 500px; height: 80px;
  }
  .envelope__contact {
    position: absolute;
    left: 215px; top: 175px;
    font-size: 9px;
    line-height: 12px;
    color: var(--ink-soft);
  }
  .envelope__contact dt { display: inline-block; width: 38px; }
  .envelope__contact dd { display: inline; }

  .brand {
    position: absolute;
    left: 36px; top: 44px;
    color: var(--ink);
  }
  .brand__line {
    display: flex;
    align-items: center;
    gap: 8px;
  }
  .brand__mark {
    width: 12px; height: 12px;
    border: 1px solid var(--ink);
  }
  .brand__name {
    font-size: 20px;
    line-height: 24px;
    font-weight: 400;
  }
  .tagline {
    position: absolute;
    left: 36px; top: 76px;
    font-size: 11px;
    line-height: 14px;
    color: var(--ink-soft);
  }
</style>
</head>
<body>
  <section class="envelope envelope--back" aria-label="Envelope back">
    <svg class="envelope__flap" viewBox="0 0 500 80" role="img" aria-label="Dark flap with repeating decorative pattern">
      <polygon points="0,0 500,0 500,62 480,80 20,80 0,62" fill="var(--flap)"/>
    </svg>
    <dl class="envelope__contact">
      <div><dt>mobile</dt><dd>0427 318 942</dd></div>
      <div><dt>phone</dt><dd>03 9512 3470</dd></div>
      <div><dd>mirren@tovell-interiors.com.au</dd></div>
    </dl>
  </section>

  <section class="envelope envelope--front" aria-label="Envelope front">
    <div class="brand">
      <div class="brand__line">
        <span class="brand__mark" aria-hidden="true"></span>
        <span class="brand__name">Tovell Interiors</span>
      </div>
    </div>
    <p class="tagline">Exquisite Furniture &amp; Furnishings</p>
  </section>
</body>
</html>
```